quote template for plumbing serivce for homeowners

Design Brief – Plumbing Quotation Document
1. Brand & Style
• Business: Plumbing (Maintenance focus, premium service)
• Positioning: Professional, trustworthy, high-end, compliant, reliable
• Tone: Clean, modern, premium trades, easy to read, confidence-building
• Colours: Use brand colours (or leave placeholders: Primary / Secondary / Accent)
• Fonts:
o Headings: Bold, clean, modern (e.g. Montserrat, Poppins, Inter)
o Body text: Simple and highly readable (e.g. Inter, Lato, Open Sans)
• Layout Feel: Structured, not cluttered, strong hierarchy, visually balanced, logical flow
• Imagery: Minimal – allow subtle plumbing or technical icons, but do not overpower text
2. Document Requirements
✅ Must Include:
Cover Page
• Logo
• Business name
• Tagline (if applicable)
• Document title: Quotation / Proposal
• Client name, site address, quote number, date
• Business contact details (phone, email, website, licence number optional)
• Optional photo banner or design strip (clean and minimal)
Section 1 – Introduction
• Short professional message thanking them, setting expectations
• Optional small “Our promise” or “What to expect” note
Section 2 – Price Options
• Must support unlimited quote sections / options (Option 1, Option 2, Option 3 etc.)
• Each option should include:
o Detailed description
o Price
o Optional tick/check icons to highlight benefits
• Layout must allow adding or removing options easily without breaking format
• Pricing to be emphasised but not overpower the description
Section 3 – Total Investment
• Clearly display:
o Subtotal
o GST
o Total
• Include optional line for:
o Deposit (if applicable)
o Payment terms (optional)
• Should stand out using contrast box or section highlight
Section 4 – Why Choose Us
Include space or icons for key trust points. Must allow content similar to:
• Licensed & insured plumbing professionals
• Lifetime labour warranty on workmanship
• Premium materials and compliant installations
• Transparent pricing, no hidden surprises
• On-time, tidy, and customer-focused
• Australian Standards compliant (KT/LR 7140)
• Local, trusted, reviewed business
Designer to create layout that supports 5–8 trust points using icons or bold highlights.
Section 5 – Terms & Conditions
Must allow a text area for:
• Quote validity
• What is/what isn’t included
• Warranty notes
• Site access requirements
• Variations clause
• Payment terms
Section 6 – Acceptance
Needs to include:
• Signature line
• Print name
• Date
• Option to tick selected option if multiple options provided
• “Approval to proceed” section
Optional Page Elements
(Include if space allows)
• Certifications or licence numbers
• Vexora review rating or testimonial section
• Before/after photo box (if relevant)
• QR code linking to website or booking page
• Small footer with company details on each page
3. Functional Requirements
• Must be:
o Easy to edit (headings, prices, options, text blocks)
o Expandable (sections must duplicate without breaking layout)
o Saveable as PDF
o Professional when printed
o Visually aligned to premium home & commercial clients
• Page numbering required (Page 1 of X)
• Consistent header or footer with business name/logo
4. Deliverables Needed
Designer to supply:
1. Master editable template (Canva, Word, or InDesign INDD)
2. PDF export version
3. Style guide (fonts, sizes, colours)
4. Instructions for duplicating option sections easily
5. Design Inspiration Keywords
• Premium trade proposal
• Clean modern layout
• Structured price options
• Trust-building visuals
• Technical but customer-friendly
• Compliant and confident
home owners
plumbing

```html
<!DOCTYPE html>
<html lang="en">
<head>
<meta charset="utf-8">
<title>Tideline Plumbing – Quotation Template</title>
<link href="https://fonts.googleapis.com/css2?family=Poppins:wght@600;700;800&family=Open+Sans:wght@400;600;700&display=swap" rel="stylesheet">
<style>
:root{
  --blue:#00b8e0;
  --yellow:#f9c254;
  --dark:#222324;
  --black:#111;
  --footer:#3c3d3f;
  --stage:#5f6061;
  --ink:#1c1c1c;
  --line:#8a8a8a;
  --photo-warm:linear-gradient(160deg,#c9a877 0%,#b07b4a 40%,#d9582a 65%,#7a5a3c 100%);
}
*{box-sizing:border-box;margin:0;padding:0}
html,body{width:1200px;height:1049px;overflow:hidden;background:var(--stage)}
body{position:relative;font-family:"Open Sans",sans-serif;color:var(--ink)}
.page{position:absolute;width:374px;height:483px;background:#fff;overflow:hidden}
.p-cover{left:26px;top:34px}
.p-cover-alt{left:411px;top:34px;background:var(--black)}
.p-one{left:797px;top:34px}
.p-two{left:26px;top:529px}
.p-three{left:411px;top:529px}
.p-four{left:797px;top:529px}
.abs{position:absolute}
.photo{position:absolute;background:var(--photo-warm)}
.brand{font-family:"Poppins",sans-serif;font-weight:800;color:var(--blue);letter-spacing:1px;display:flex;align-items:center;gap:4px}
.brand .dot{width:.55em;height:.55em;border-radius:50%;background:var(--yellow);display:inline-block}
.bizname{font-family:"Poppins",sans-serif;font-weight:700;color:var(--yellow)}
.labels{font-size:6.4px;color:var(--yellow);line-height:8.6px}
.labels-w{font-size:6.4px;color:#fff;line-height:8.6px}
.band{position:absolute;left:11px;width:355px;height:14px;background:var(--blue);color:#fff;font-family:"Poppins",sans-serif;font-weight:700;font-size:12px;line-height:14px;padding-left:13px}
.body-s{font-size:5.4px;line-height:6.6px;color:#222}
.opt-title{font-family:"Poppins",sans-serif;font-weight:700;color:var(--blue)}
.ptable{position:absolute;left:23px;width:330px;border:0.6px solid var(--line)}
.ptable .row{display:grid;grid-template-columns:56px 204px 70px;border-top:0.6px solid var(--line);height:9px}
.ptable .row:first-child{border-top:0;height:16px}
.ptable .row div{border-left:0.6px solid var(--line);font-size:6px;line-height:16px;padding-left:2px}
.ptable .row div:first-child{border-left:0}
.ptable .head .opt-title{font-size:8px}
.ptable .head .price{font-weight:700}
.benefits{position:absolute;left:25px;font-size:6.2px;line-height:9.1px}
.tick{display:flex;align-items:center;gap:3px}
.tick svg{width:6px;height:6px}
.footer{position:absolute;left:23px;top:457px;width:331px;height:14px;background:var(--footer);color:#fff;font-size:4.6px;display:flex;align-items:center;padding:0 5px;gap:7px;white-space:nowrap}
.footer .brand{font-size:7px;letter-spacing:.3px}
.footer .pg{margin-left:auto;font-weight:600}
.totals{position:absolute;left:22px;top:46px;width:329px;border:0.6px solid var(--line);font-size:6.2px}
.totals .row{display:grid;grid-template-columns:255px 74px;height:10.3px;border-top:0.6px solid var(--line)}
.totals .row:first-child{border-top:0}
.totals .row div{padding-left:2px;line-height:10.3px}
.totals .row div+div{border-left:0.6px solid var(--line)}
.totals .row.tall{height:17px}
.trust{position:absolute;display:flex;align-items:center}
.trust .drop{width:24px;height:26px;position:relative;z-index:2}
.trust .label{margin-left:-5px;width:103px;height:16px;background:var(--yellow);font-family:"Poppins",sans-serif;font-weight:600;font-size:5.8px;line-height:6.2px;padding:2px 0 0 12px;color:var(--ink)}
.tc{position:absolute;width:106px;height:130px;background:var(--yellow);padding:58px 4px 0 4px}
.tc h3{font-family:"Poppins",sans-serif;font-weight:700;font-size:8.6px;line-height:10px;margin-bottom:9px}
.tc p{font-size:5.9px;line-height:7.2px}
.field-l{position:absolute;font-size:6.4px}
.box{position:absolute;height:9px;border:0.6px solid #777}
.tcard{position:absolute;width:88px;height:121px;border:1px solid #333;border-radius:10px;font-size:4.4px;display:flex;align-items:center;justify-content:center}
.tinfo{position:absolute;width:64px}
.tinfo .nm{font-family:"Poppins",sans-serif;font-weight:700;font-size:7px}
.tinfo .sub{font-size:4px;margin-top:1px;padding-bottom:5px;border-bottom:0.6px solid #555}
.tinfo .stars{font-size:8px;margin:5px 0 4px 5px;letter-spacing:.5px}
.tinfo .q{font-size:6px;line-height:7.3px}
.ba{position:absolute;background:linear-gradient(160deg,#b9a88c,#8a7b63 60%,#d8cfc0);color:#fff;font-family:"Poppins",sans-serif;font-weight:600;display:flex;align-items:flex-end;justify-content:flex-end;padding:0 3px 1px 0;font-size:6.5px}
.ba.small{font-size:7px;justify-content:center}
</style>
</head>
<body>

<!-- Cover -->
<section class="page p-cover">
  <div class="photo" role="img" aria-label="Photo of a gloved hand turning an adjustable wrench on copper pipework" style="inset:0"></div>
  <svg class="abs" style="inset:0;width:374px;height:483px" viewBox="0 0 639 826" preserveAspectRatio="none">
    <path d="M0 0H639V230C420 215 220 270 0 410Z" fill="#222324"/>
    <path d="M0 335C210 240 420 80 639 0C470 110 260 280 0 400Z" fill="#00b8e0"/>
    <path d="M70 372C250 262 450 224 639 234" stroke="#f9c254" stroke-width="6" fill="none"/>
  </svg>
  <div class="brand abs" style="left:23px;top:24px;font-size:24px">TIDELINE<span class="dot"></span></div>
  <div class="bizname abs" style="left:24px;top:72px;font-size:12.5px">Tideline Plumbing</div>
  <div class="labels abs" style="left:24px;top:88px">PHONE:<br>EMAIL:<br>WEBSITE:<br>LICENCE NUMBER<br>OPTIONAL:</div>
  <div class="labels-w abs" style="left:247px;top:74px;line-height:9px">CLIENT NAME:<br>SITE ADDRESS:<br>QUOTE NUMBER:<br>DATE:</div>
  <div class="abs" style="left:75px;top:372px;font-family:'Poppins',sans-serif;font-weight:700;font-size:21px;white-space:nowrap"><span style="color:var(--blue)">Quotation</span> <span style="color:var(--yellow)">/ Proposal</span></div>
</section>

<!-- Cover alternative -->
<section class="page p-cover-alt">
  <div class="photo" role="img" aria-label="Photo of a gloved hand turning an adjustable wrench on copper pipework" style="left:0;top:0;width:374px;height:329px"></div>
  <div class="abs" style="left:15px;top:0;width:3px;height:483px;background:var(--blue)"></div>
  <div class="abs" style="left:20px;top:318px;transform:rotate(-90deg);transform-origin:0 0;font-family:'Poppins',sans-serif;font-weight:700;font-size:22px;letter-spacing:.5px;white-space:nowrap;line-height:22px;color:var(--yellow)">QUOTATION <span style="color:var(--blue)">/ PROPOSAL</span></div>
  <div class="brand abs" style="left:36px;top:342px;font-size:24px">TIDELINE<span class="dot"></span></div>
  <div class="bizname abs" style="left:37px;top:397px;font-size:13px">Tideline Plumbing</div>
  <div class="labels-w abs" style="left:37px;top:421px">PHONE:<br>EMAIL:<br>WEBSITE:<br>LICENCE NUMBER<br>OPTIONAL:</div>
  <div class="box" style="left:63px;top:422px;width:84px;border-color:#ccc"></div>
  <div class="box" style="left:61px;top:431px;width:86px;border-color:#ccc"></div>
  <div class="box" style="left:68px;top:439px;width:79px;border-color:#ccc"></div>
  <div class="box" style="left:96px;top:448px;width:51px;border-color:#ccc"></div>
  <div class="box" style="left:74px;top:456px;width:73px;border-color:#ccc"></div>
  <div class="labels-w abs" style="left:171px;top:421px;line-height:11.7px">CLIENT NAME:<br>SITE ADDRESS:<br>QUOTE NUMBER:<br>DATE:</div>
  <div class="box" style="left:216px;top:422px;width:115px;border-color:#ccc"></div>
  <div class="box" style="left:216px;top:434px;width:115px;border-color:#ccc"></div>
  <div class="box" style="left:224px;top:445px;width:107px;border-color:#ccc"></div>
  <div class="box" style="left:193px;top:457px;width:138px;border-color:#ccc"></div>
</section>

<!-- Page 1: Introduction & price options -->
<section class="page p-one">
  <div class="band" style="top:21px">Introduction</div>
  <p class="body-s abs" style="left:26px;top:40px;width:320px">Lorem ipsum dolor sit amet, consectetuer adipiscing elit, sed diam nonummy nibh euismod tincidunt ut laoreet dolore magna aliquam erat volutpat. Ut wisi enim ad minim veniam, quis nostrud exerci tation ullamcorper suscipit lobortis nisl ut aliquip ex ea commodo consequat.</p>
  <p class="body-s abs" style="left:26px;top:68px;font-weight:700">Our promise</p>
  <p class="body-s abs" style="left:26px;top:77px;width:320px">Lorem ipsum dolor sit amet, consectetuer adipiscing elit, sed diam nonummy nibh euismod tincidunt ut laoreet dolore magna aliquam erat volutpat. Ut wisi enim ad minim veniam, quis nostrud exerci tation ullamcorper suscipit lobortis nisl ut aliquip ex ea commodo consequat.</p>
  <div class="band" style="top:116px">Price Options</div>
  <div class="opt-title abs" style="left:25px;top:137px;font-size:9px">Option</div>

  <div class="ptable" style="top:156px">
    <div class="row head"><div class="opt-title">Option 1</div><div>Detailed description</div><div class="price">PRICE</div></div>
    <div class="row"><div></div><div></div><div></div></div><div class="row"><div></div><div></div><div></div></div>
    <div class="row"><div></div><div></div><div></div></div><div class="row"><div></div><div></div><div></div></div>
  </div>
  <div class="benefits" style="top:211px">Benefits:
    <div class="tick"><svg viewBox="0 0 10 10"><circle cx="5" cy="5" r="4.3" fill="none" stroke="#222" stroke-width="1"/><path d="M3 5.2l1.4 1.4L7.2 3.8" fill="none" stroke="#222" stroke-width="1"/></svg>Lorem ipsum dolor sit amet</div>
    <div class="tick"><svg viewBox="0 0 10 10"><circle cx="5" cy="5" r="4.3" fill="none" stroke="#222" stroke-width="1"/><path d="M3 5.2l1.4 1.4L7.2 3.8" fill="none" stroke="#222" stroke-width="1"/></svg>Lorem ipsum dolor sit amet</div>
    <div class="tick"><svg viewBox="0 0 10 10"><circle cx="5" cy="5" r="4.3" fill="none" stroke="#222" stroke-width="1"/><path d="M3 5.2l1.4 1.4L7.2 3.8" fill="none" stroke="#222" stroke-width="1"/></svg>Lorem ipsum dolor sit amet</div>
  </div>

  <div class="ptable" style="top:253px">
    <div class="row head"><div class="opt-title">Option 2</div><div>Detailed description</div><div class="price">PRICE</div></div>
    <div class="row"><div></div><div></div><div></div></div><div class="row"><div></div><div></div><div></div></div>
    <div class="row"><div></div><div></div><div></div></div><div class="row"><div></div><div></div><div></div></div>
  </div>
  <div class="benefits" style="top:308px">Benefits:
    <div class="tick"><svg viewBox="0 0 10 10"><circle cx="5" cy="5" r="4.3" fill="none" stroke="#222" stroke-width="1"/><path d="M3 5.2l1.4 1.4L7.2 3.8" fill="none" stroke="#222" stroke-width="1"/></svg>Lorem ipsum dolor sit amet</div>
    <div class="tick"><svg viewBox="0 0 10 10"><circle cx="5" cy="5" r="4.3" fill="none" stroke="#222" stroke-width="1"/><path d="M3 5.2l1.4 1.4L7.2 3.8" fill="none" stroke="#222" stroke-width="1"/></svg>Lorem ipsum dolor sit amet</div>
    <div class="tick"><svg viewBox="0 0 10 10"><circle cx="5" cy="5" r="4.3" fill="none" stroke="#222" stroke-width="1"/><path d="M3 5.2l1.4 1.4L7.2 3.8" fill="none" stroke="#222" stroke-width="1"/></svg>Lorem ipsum dolor sit amet</div>
  </div>

  <div class="ptable" style="top:354px">
    <div class="row head"><div class="opt-title">Option 3</div><div>Detailed description</div><div class="price">PRICE</div></div>
    <div class="row"><div></div><div></div><div></div></div><div class="row"><div></div><div></div><div></div></div>
    <div class="row"><div></div><div></div><div></div></div><div class="row"><div></div><div></div><div></div></div>
  </div>
  <div class="benefits" style="top:408px">Benefits:
    <div class="tick"><svg viewBox="0 0 10 10"><circle cx="5" cy="5" r="4.3" fill="none" stroke="#222" stroke-width="1"/><path d="M3 5.2l1.4 1.4L7.2 3.8" fill="none" stroke="#222" stroke-width="1"/></svg>Lorem ipsum dolor sit amet</div>
    <div class="tick"><svg viewBox="0 0 10 10"><circle cx="5" cy="5" r="4.3" fill="none" stroke="#222" stroke-width="1"/><path d="M3 5.2l1.4 1.4L7.2 3.8" fill="none" stroke="#222" stroke-width="1"/></svg>Lorem ipsum dolor sit amet</div>
    <div class="tick"><svg viewBox="0 0 10 10"><circle cx="5" cy="5" r="4.3" fill="none" stroke="#222" stroke-width="1"/><path d="M3 5.2l1.4 1.4L7.2 3.8" fill="none" stroke="#222" stroke-width="1"/></svg>Lorem ipsum dolor sit amet</div>
  </div>

  <div class="footer"><span class="brand">TIDELINE</span><span style="margin-left:30px">Phone: 0000000000 &nbsp;|&nbsp; Website: www.tidelineplumbing.com &nbsp;|&nbsp; Licence Number: 00000000000</span><span class="pg">Page 1 of 6</span></div>
</section>

<!-- Page 2: Total investment & why choose us -->
<section class="page p-two">
  <div class="band" style="top:21px">Total Investment</div>
  <div class="totals">
    <div class="row"><div>Subtotal:</div><div>000000000</div></div>
    <div class="row"><div>GST:</div><div>0000</div></div>
    <div class="row"><div>Total:</div><div>00000000</div></div>
    <div class="row"><div>Deposit (if applicable):</div><div>000000000</div></div>
    <div class="row tall"><div>Payment terms (optional):</div><div></div></div>
  </div>
  <div class="band" style="top:122px">Why Choose Us</div>
  <div class="photo" role="img" aria-label="Photo of copper pipe fittings, a pipe wrench and cutter lying on technical plans" style="left:0;top:243px;width:374px;height:209px;background:linear-gradient(150deg,#e8e8e6 0%,#d9d6d1 35%,#c27a52 55%,#b8432f 80%,#8d8d8d 100%)"></div>

  <div class="trust" style="left:21px;top:162px"><svg class="drop" viewBox="0 0 24 26"><path d="M12 0C15 6 22 11 22 17a10 9 0 0 1-20 0C2 11 9 6 12 0Z" fill="#f9c254"/><rect x="8" y="12" width="8" height="8" fill="none" stroke="#222" stroke-width="1"/></svg><div class="label">Licensed &amp; insured<br>plumbing professionals</div></div>
  <div class="trust" style="left:21px;top:197px"><svg class="drop" viewBox="0 0 24 26"><path d="M12 0C15 6 22 11 22 17a10 9 0 0 1-20 0C2 11 9 6 12 0Z" fill="#f9c254"/><circle cx="12" cy="16" r="4.5" fill="none" stroke="#222" stroke-width="1"/><path d="M10 16l1.5 1.5 2.5-3" fill="none" stroke="#222" stroke-width="1"/></svg><div class="label">Lifetime labour warranty<br>on workmanship</div></div>
  <div class="trust" style="left:21px;top:232px"><svg class="drop" viewBox="0 0 24 26"><path d="M12 0C15 6 22 11 22 17a10 9 0 0 1-20 0C2 11 9 6 12 0Z" fill="#f9c254"/><circle cx="12" cy="16" r="5" fill="none" stroke="#222" stroke-width="1"/></svg><div class="label">Premium materials and<br>compliant installations</div></div>
  <div class="trust" style="left:21px;top:270px"><svg class="drop" viewBox="0 0 24 26"><path d="M12 0C15 6 22 11 22 17a10 9 0 0 1-20 0C2 11 9 6 12 0Z" fill="#f9c254"/><path d="M8 18l5-5h3v3l-5 5Z" fill="none" stroke="#222" stroke-width="1"/></svg><div class="label">Transparent pricing,<br>no hidden surprises</div></div>
  <div class="trust" style="left:180px;top:162px"><svg class="drop" viewBox="0 0 24 26"><path d="M12 0C15 6 22 11 22 17a10 9 0 0 1-20 0C2 11 9 6 12 0Z" fill="#f9c254"/><circle cx="12" cy="16" r="4.5" fill="none" stroke="#222" stroke-width="1"/><path d="M12 13.5V16h2" fill="none" stroke="#222" stroke-width="1"/></svg><div class="label">On-time, tidy, and<br>customer-focused</div></div>
  <div class="trust" style="left:180px;top:197px"><svg class="drop" viewBox="0 0 24 26"><path d="M12 0C15 6 22 11 22 17a10 9 0 0 1-20 0C2 11 9 6 12 0Z" fill="#f9c254"/><path d="M12 11l4 2v3c0 2-2 4-4 5-2-1-4-3-4-5v-3Z" fill="none" stroke="#222" stroke-width="1"/></svg><div class="label">Australian Standards<br>compliant (KT/LR 7140)</div></div>
  <div class="trust" style="left:180px;top:233px"><svg class="drop" viewBox="0 0 24 26"><path d="M12 0C15 6 22 11 22 17a10 9 0 0 1-20 0C2 11 9 6 12 0Z" fill="#f9c254"/><circle cx="9.5" cy="15" r="1.8" fill="none" stroke="#222" stroke-width="1"/><circle cx="14.5" cy="15" r="1.8" fill="none" stroke="#222" stroke-width="1"/><path d="M7 20c1-2 4-2 5 0M12 20c1-2 4-2 5 0" fill="none" stroke="#222" stroke-width="1"/></svg><div class="label">Local, trusted, reviewed<br>business</div></div>

  <div class="footer" style="top:457px"><span class="brand">TIDELINE</span><span style="margin-left:30px">Phone: 0000000000 &nbsp;|&nbsp; Website: www.tidelineplumbing.com &nbsp;|&nbsp; Licence Number: 00000000000</span><span class="pg">Page 2 of 6</span></div>
</section>

<!-- Page 3: Terms & acceptance -->
<section class="page p-three">
  <div class="band" style="top:21px">Terms &amp; Conditions</div>
  <div class="tc" style="left:19px;top:50px"><h3>Quote validity</h3><p>Lorem ipsum dolor sit amet, consectetuer adipiscing elit, sed diam nonummy nibh euismod tincidunt ut laoreet dolore magna aliquam erat volutpat.</p></div>
  <div class="tc" style="left:132px;top:50px;width:111px"><h3>What is/what isn’t included</h3><p>Lorem ipsum dolor sit amet, consectetuer adipiscing elit, sed diam nonummy nibh euismod tincidunt ut laoreet dolore magna aliquam erat volutpat.</p></div>
  <div class="tc" style="left:249px;top:50px"><h3>Warranty notes</h3><p>Lorem ipsum dolor sit amet, consectetuer adipiscing elit, sed diam nonummy nibh euismod tincidunt ut laoreet dolore magna aliquam erat volutpat.</p></div>
  <div class="tc" style="left:19px;top:188px;height:131px;padding-top:57px"><h3>Site access require-ments</h3><p>Lorem ipsum dolor sit amet, consectetuer adipiscing elit, sed diam nonummy nibh euismod tincidunt ut laoreet dolore magna aliquam erat volutpat.</p></div>
  <div class="tc" style="left:132px;top:188px;width:111px;height:131px;padding-top:57px"><h3>Variations clause</h3><p>Lorem ipsum dolor sit amet, consectetuer adipiscing elit, sed diam nonummy nibh euismod tincidunt ut laoreet dolore magna aliquam erat volutpat.</p></div>
  <div class="tc" style="left:249px;top:188px;height:131px;padding-top:57px"><h3>Payment terms</h3><p>Lorem ipsum dolor sit amet, consectetuer adipiscing elit, sed diam nonummy nibh euismod tincidunt ut laoreet dolore magna aliquam erat volutpat.</p></div>

  <div class="band" style="top:331px">Acceptance</div>
  <div class="field-l" style="left:16px;top:359px">Print name:</div><div class="box" style="left:54px;top:359px;width:129px"></div>
  <div class="field-l" style="left:16px;top:377px">Print name:</div><div class="box" style="left:54px;top:377px;width:129px"></div>
  <div class="field-l" style="left:191px;top:359px;font-weight:600">Signature line:</div><div class="box" style="left:240px;top:359px;width:102px"></div>
  <div class="field-l" style="left:191px;top:377px;font-weight:600">Signature line:</div><div class="box" style="left:240px;top:377px;width:102px"></div>
  <div class="field-l" style="left:191px;top:396px">Date:</div><div class="box" style="left:211px;top:396px;width:131px"></div>
  <div class="field-l" style="left:191px;top:414px">Approval to proceed</div>
  <div class="benefits" style="left:16px;top:396px">Selected option
    <div class="tick"><svg viewBox="0 0 10 10"><circle cx="5" cy="5" r="4.3" fill="none" stroke="#222" stroke-width="1"/><path d="M3 5.2l1.4 1.4L7.2 3.8" fill="none" stroke="#222" stroke-width="1"/></svg>Lorem ipsum dolor sit amet</div>
    <div class="tick"><svg viewBox="0 0 10 10"><circle cx="5" cy="5" r="4.3" fill="none" stroke="#222" stroke-width="1"/><path d="M3 5.2l1.4 1.4L7.2 3.8" fill="none" stroke="#222" stroke-width="1"/></svg>Lorem ipsum dolor sit amet</div>
    <div class="tick"><svg viewBox="0 0 10 10"><circle cx="5" cy="5" r="4.3" fill="none" stroke="#222" stroke-width="1"/><path d="M3 5.2l1.4 1.4L7.2 3.8" fill="none" stroke="#222" stroke-width="1"/></svg>Lorem ipsum dolor sit amet</div>
  </div>
  <div class="footer"><span class="brand">TIDELINE</span><span style="margin-left:30px">Phone: 0000000000 &nbsp;|&nbsp; Website: www.tidelineplumbing.com &nbsp;|&nbsp; Licence Number: 00000000000</span><span class="pg">Page 3 of 6</span></div>
</section>

<!-- Page 4: Testimonials -->
<section class="page p-four">
  <div class="band" style="top:21px">Testimonial</div>
  <div class="tcard" style="left:20px;top:50px">Image</div>
  <div class="tinfo" style="left:120px;top:68px"><div class="nm">NAME HERE</div><div class="sub">Lorem ipsum</div><div class="stars">★★★☆☆</div><div class="q">“Lorem ipsum dolor sit amet, consectetuer adipiscing elit, sed diam nonummy nibh.”</div></div>
  <div class="tcard" style="left:191px;top:50px">Image</div>
  <div class="tinfo" style="left:291px;top:68px"><div class="nm">NAME HERE</div><div class="sub">Lorem ipsum</div><div class="stars">★★★☆☆</div><div class="q">“Lorem ipsum dolor sit amet, consectetuer adipiscing elit, sed diam nonummy nibh.”</div></div>
  <div class="tcard" style="left:20px;top:182px">Image</div>
  <div class="tinfo" style="left:120px;top:200px"><div class="nm">NAME HERE</div><div class="sub">Lorem ipsum</div><div class="stars">★★★☆☆</div><div class="q">“Lorem ipsum dolor sit amet, consectetuer adipiscing elit, sed diam nonummy nibh.”</div></div>
  <div class="tcard" style="left:191px;top:182px">Image</div>
  <div class="tinfo" style="left:291px;top:200px"><div class="nm">NAME HERE</div><div class="sub">Lorem ipsum</div><div class="stars">★★★☆☆</div><div class="q">“Lorem ipsum dolor sit amet, consectetuer adipiscing elit, sed diam nonummy nibh.”</div></div>

  <div class="ba" role="img" aria-label="Before photo of an old pipe under a basin" style="left:20px;top:328px;width:78px;height:119px">Before</div>
  <div class="ba" role="img" aria-label="After photo of a new pipe under a basin" style="left:100px;top:328px;width:79px;height:119px">After</div>
  <div class="ba small" role="img" aria-label="Before photo of wall plumbing" style="left:185px;top:329px;width:41px;height:55px">Before</div>
  <div class="ba small" role="img" aria-label="After photo of wall plumbing" style="left:230px;top:329px;width:39px;height:55px">After</div>
  <div class="ba small" role="img" aria-label="Before photo of a bathroom" style="left:185px;top:389px;width:41px;height:58px;font-size:5px">Before</div>
  <div class="ba small" role="img" aria-label="After photo of a renovated bathroom" style="left:230px;top:389px;width:39px;height:58px;font-size:5px">After</div>

  <div class="footer"><span class="brand">TIDELINE</span><span style="margin-left:30px">Phone: 0000000000 &nbsp;|&nbsp; Website: www.tidelineplumbing.com &nbsp;|&nbsp; Licence Number: 00000000000</span><span class="pg">Page 4 of 6</span></div>
</section>

</body>
</html>
```